Paper and board wholesaler needs business card design for managers

We need a business card design that incorporates bordo red, white and/ or grey colors. The business card has to have our "VELON" logo and our partners paper group logo that we are part of - "ROSKU group". Both of the logos should be applied to the business card according to the guidelines for the usage of the logo that have been added in the uploaded files.
The letters (information on the card) should be easily readable, so no "shiny" or "glossy" text.
Besides the two logos, the business card needs to contain information for the respective person:
1) Name, Surname,
2) Job position (e.g. "sales represantative"),
3) E-mail,
4) Phone number,
5) text: "Kartonu Mājvieta (VELON)" LTD
6) our office address "Riga, Sārtaines street 42".
(also could have) 7) our homepage address "www.velon.lv"
Holiday season, so have a lot of tasks to take care of and not as much time to check SketchHarbor as often.
1) Name, Surname, 2) Job position (e.g. "sales represantative"), 3) E-mail, 4) Phone number, 5) text: "Kartonu Mājvieta (VELON)" LTD 6) our office address "Riga, Sārtaines street 42". (also could have) 7) our homepage address "www.velon.lv"
Other font styles liked:
- Josefin Sans

```html
<!DOCTYPE html>
<html lang="en">
<head>
<meta charset="utf-8">
<title>VELON business card</title>
<link href="https://fonts.googleapis.com/css2?family=Poppins:wght@400;500;600&display=swap" rel="stylesheet">
<style>
  :root {
    --bordo: #7e3236;
    --bordo-dark: #6a282c;
    --paper: #ffffff;
    --stage: #2b2b2b;
    --partner-green: #127a57;
    --ink-grey: #9a9a9a;
  }
  * { box-sizing: border-box; margin: 0; padding: 0; }
  html, body { width: 1200px; height: 820px; overflow: hidden; }
  body {
    background: var(--stage);
    font-family: "Poppins", sans-serif;
    display: flex;
    align-items: center;
    justify-content: center;
    gap: 40px;
  }
  .card {
    width: 540px;
    height: 310px;
    position: relative;
    border-radius: 3px;
    overflow: hidden;
  }
  /* Front side */
  .card-front { background: var(--paper); color: var(--bordo); }
  .person { position: absolute; left: 40px; top: 118px; }
  .person-name { font-size: 19px; font-weight: 600; letter-spacing: 0.3px; line-height: 1.1; }
  .person-role { font-size: 14px; font-weight: 400; line-height: 1.3; }
  .contacts { position: absolute; left: 40px; top: 178px; list-style: none; }
  .contacts li { display: flex; align-items: center; gap: 8px; font-size: 14px; line-height: 19px; }
  .contacts svg { width: 12px; height: 12px; flex: none; }
  .company { position: absolute; left: 40px; bottom: 26px; font-size: 14px; line-height: 19px; }
  .brand-front { position: absolute; right: 44px; top: 34px; width: 230px; text-align: center; }
  .brand-square {
    width: 64px; height: 64px;
    border: 3px solid var(--bordo);
    margin: 0 auto 22px;
  }
  .brand-name {
    font-size: 22px; font-weight: 600;
    letter-spacing: 24px; margin-right: -24px;
  }
  .partner {
    position: absolute; right: 40px; bottom: 92px;
    display: flex; align-items: center; gap: 8px;
    color: var(--partner-green);
    font-size: 20px; font-weight: 500;
  }
  .partner-dot { width: 22px; height: 22px; border-radius: 50%; background: var(--partner-green); }
  /* Back side */
  .card-back { background: var(--bordo); color: var(--paper); }
  .back-square {
    position: absolute; left: 34px; top: 40px;
    width: 230px; height: 230px;
    border: 8px solid var(--bordo-dark);
    box-shadow: inset 0 0 0 2px rgba(255, 90, 95, 0.35);
  }
  .back-name {
    position: absolute; left: 300px; top: 136px;
    font-size: 24px; font-weight: 600;
    letter-spacing: 20px;
  }
</style>
</head>
<body>
  <section class="card card-front" aria-label="Business card front">
    <div class="person">
      <p class="person-name">MAREKS OZOLIŅŠ</p>
      <p class="person-role">Managing Director</p>
    </div>
    <ul class="contacts">
      <li>
        <svg viewBox="0 0 12 12" aria-hidden="true"><path d="M2.5 1l2 2.2-1 1.3c.6 1.3 1.6 2.3 3 3l1.3-1L10 8.5 9 10.5C5 10.3 1.7 7 1.5 3z" fill="var(--bordo)"/></svg>
        067-480 215 903
      </li>
      <li>
        <svg viewBox="0 0 12 12" aria-hidden="true"><rect x="0.5" y="2" width="11" height="8" fill="var(--bordo)"/><path d="M0.8 2.4L6 6.6l5.2-4.2" stroke="#fff" stroke-width="1" fill="none"/></svg>
        hello@velonmail.com
      </li>
      <li>
        <svg viewBox="0 0 12 12" aria-hidden="true"><g fill="none" stroke="var(--bordo)" stroke-width="1.1"><circle cx="6" cy="6" r="5"/><ellipse cx="6" cy="6" rx="2.2" ry="5"/><path d="M1 6h10M2 3.5h8M2 8.5h8"/></g></svg>
        www.velon.lv
      </li>
    </ul>
    <p class="company">Kartonu Mājvieta (VELON) LTD<br>Riga, Sārtaines street 42</p>
    <div class="brand-front">
      <div class="brand-square"></div>
      <p class="brand-name">VELON</p>
    </div>
    <div class="partner">
      <span class="partner-dot"></span>
      <span>ROSKU group</span>
    </div>
  </section>

  <section class="card card-back" aria-label="Business card back">
    <div class="back-square"></div>
    <p class="back-name">VELON</p>
  </section>
</body>
</html>
```